TQ Regulatory Partners - Biz Card - Re-do

I would like a re-do on my business card.

See my Internet site - tqregpartners.com

1) Remove direct phone line.
2) Add company moto - integrity, diligence, and excellence
3) Add Consulting Services listing:
-Benefit Technology
-ERISA Compliance
-Contract/Vendor Management
-Human Resource/Payroll
-Medical/Prescription Drug
-Integrated Leave of Absence

Target Market(s)

Employee benefit consulting and insurance purchasers, Usually human resource executives

Industry/Entity Type

Human Resource

Contact Information for Business Card

Same business card color scheme, logo,

Font styles to use
Sans Serif

Requirements
Must have
• Same color scheme and logo. Remove direct phone number. Keep all numbers, internet address.

```html
<!DOCTYPE html>
<html lang="en">
<head>
<meta charset="utf-8">
<title>TQ Regulatory Partners – Business Card</title>
<link href="https://fonts.googleapis.com/css2?family=Lato:wght@400;700&display=swap" rel="stylesheet">
<style>
  :root{
    --backdrop:#141414;
    --card:#1f1f1f;
    --card-edge:#2a2a2a;
    --ink-white:#f2f2f2;
    --ink-grey:#8a8a8a;
    --mark-grey:#6f6f6f;
    --rule:#e6e6e6;
  }
  *{margin:0;padding:0;box-sizing:border-box}
  html,body{width:1200px;height:900px;overflow:hidden;background:var(--backdrop)}
  body{font-family:"Lato",Arial,sans-serif;color:var(--ink-white);position:relative}
  .card{
    position:absolute;left:280px;width:640px;height:366px;
    background:linear-gradient(135deg,var(--card) 0%,#262626 60%,#1c1c1c 100%);
    border:1px solid var(--card-edge);
    box-shadow:0 18px 40px rgba(0,0,0,.6);
  }
  .card--front{top:52px}
  .card--back{top:482px}

  /* front */
  .front__brand{position:absolute;top:40px;left:0;right:0;text-align:center}
  .brand-dot{display:block;width:86px;height:86px;border-radius:50%;margin:0 auto 14px;background:var(--mark-grey)}
  .brand-name{font-size:36px;font-weight:400;color:var(--ink-grey);letter-spacing:.5px}
  .services{position:absolute;top:218px;left:0;right:0;text-align:center;font-size:17px;line-height:25px;color:var(--ink-white);letter-spacing:.3px}
  .motto{position:absolute;top:310px;left:0;right:0;text-align:center;font-size:14px;letter-spacing:2px;text-transform:uppercase;color:var(--ink-grey)}

  /* back */
  .back__brand{position:absolute;left:40px;top:128px;display:flex;align-items:center;gap:18px}
  .back__brand .brand-dot{width:90px;height:90px;margin:0;background:var(--ink-white)}
  .back__brand .brand-name{font-size:27px;line-height:32px;width:190px}
  .divider{position:absolute;left:352px;top:120px;width:2px;height:200px;background:var(--rule)}
  .contact{position:absolute;left:382px;top:118px}
  .contact__name{font-size:25px;font-weight:700;color:var(--ink-grey);letter-spacing:1px;text-transform:uppercase}
  .contact__title{font-size:16px;margin-top:2px}
  .contact__address{font-size:17px;line-height:23px;margin-top:16px}
  .contact__list{list-style:none;margin-top:12px;font-size:17px;line-height:26px}
  .contact__list li{display:flex;align-items:center;gap:10px}
  .contact__list svg{width:13px;height:13px;flex:none}
</style>
</head>
<body>

<section class="card card--front" aria-label="Card front">
  <div class="front__brand">
    <span class="brand-dot"></span>
    <p class="brand-name">TQ Regulatory Partners</p>
  </div>
  <p class="services">
    Benefit Technology | ERISA Compliance<br>
    Contract/Vendor Management | Human Resource/Payroll<br>
    Medical/Prescription Drug | Integrated Leave of Absence
  </p>
  <p class="motto">Integrity, Diligence, and Excellence</p>
</section>

<section class="card card--back" aria-label="Card back">
  <div class="back__brand">
    <span class="brand-dot"></span>
    <p class="brand-name">TQ Regulatory Partners</p>
  </div>
  <span class="divider"></span>
  <div class="contact">
    <p class="contact__name">Daniel Ashford</p>
    <p class="contact__title">President</p>
    <p class="contact__address">410 Harbor Street SE, Suite 200<br>Lakeview, MI 49100</p>
    <ul class="contact__list">
      <li>
        <svg viewBox="0 0 16 16" aria-hidden="true"><path d="M4 1l3 3-2 2c1 2 3 4 5 5l2-2 3 3-2 2C7 14 2 9 2 3z" fill="none" stroke="#8a8a8a" stroke-width="1.4"/></svg>
        555.204.7731
      </li>
      <li>
        <svg viewBox="0 0 16 16" aria-hidden="true"><rect x="4" y="1" width="8" height="5" fill="#8a8a8a"/><rect x="1" y="6" width="14" height="6" fill="#8a8a8a"/><rect x="4" y="11" width="8" height="4" fill="#8a8a8a"/></svg>
        555.204.7732
      </li>
      <li>
        <svg viewBox="0 0 16 16" aria-hidden="true"><rect x="1" y="3" width="14" height="10" fill="none" stroke="#8a8a8a" stroke-width="1.4"/><path d="M1 3l7 6 7-6" fill="none" stroke="#8a8a8a" stroke-width="1.4"/></svg>
        dashford@tqregpartners.com
      </li>
      <li>
        <svg viewBox="0 0 16 16" aria-hidden="true"><circle cx="8" cy="8" r="6.5" fill="none" stroke="#8a8a8a" stroke-width="1.3"/><ellipse cx="8" cy="8" rx="3" ry="6.5" fill="none" stroke="#8a8a8a" stroke-width="1.1"/><path d="M1.5 8h13" stroke="#8a8a8a" stroke-width="1.1"/></svg>
        www.tqregpartners.com
      </li>
    </ul>
  </div>
</section>

</body>
</html>
```